LV Business Card NEEDED

Larch Vantage is a finance brokering company that provide lending advise to consumer, business, corporate, and property developer for all their financing needs.

We source and match customer needs in Home Loan, Business Loan, Commercial Property Loan, Assets Finance, and other banking related services. It is a market with full of loans! But we specialise in more complex loan structure and our client base are more business and corporate level. Our suppliers are Banks and large Financial Institution where these business card will go to.

We have a great deal of Asian clients, therefore the card need to also include Chinese language together with English.

Refer to attached file for logo and content requirements.

We are looking for designs with the following ingredients:
* Innovative & Creative
* Professional
* Trust & Security

Please pick colours that will compliment the colours of the company logo.

Please provide a unique design, for example the edge of the card is rounded or corner cut off.

Company logo uploaded.

Please commence submitting your design.

Target Market(s)

Target audiences are businessmen, corporate, and property developer. And also a great deal of Chinese clients.

Industry/Entity Type

Finance

Contact Information for Business Card

Larch Vantage Pty. Ltd.
Morris Pelham
Director
Suite 27, 3-9 Quenby St. Wendale NSW 2188

Requirements
Must have
• Double sided design

```html
<!DOCTYPE html>
<html lang="en">
<head>
<meta charset="utf-8">
<title>Larch Vantage – Business Card</title>
<link rel="stylesheet" href="https://fonts.googleapis.com/css2?family=Cinzel:wght@400&family=Nunito+Sans:wght@300;400&family=Noto+Serif+TC:wght@600&display=swap">
<style>
  :root {
    --page: #ffffff;
    --card-front: #ffffff;
    --card-border: #c4c4c4;
    --card-back: #152144;
    --ink: #1d1d1d;
    --label: #c09a86;
    --address: #b4b4b4;
    --rule-front: #a8a8a8;
    --brand-back: #4f86b8;
    --glow: rgba(22, 120, 190, 0.75);
    --mark-grey: #c9cbcd;
    --tagline: #ffffff;
  }
  * { margin: 0; padding: 0; box-sizing: border-box; }
  html, body { width: 1200px; height: 1000px; overflow: hidden; background: var(--page); }
  .canvas { position: relative; width: 1200px; height: 1000px; }

  .card { position: absolute; left: 260px; width: 680px; height: 393px; border-radius: 28px; overflow: hidden; }
  .card--front { top: 85px; background: var(--card-front); border: 3px solid var(--card-border); }
  .card--back { top: 523px; background: var(--card-back); }

  .brand { position: absolute; text-align: center; }
  .brand__mark { display: block; margin: 0 auto; border-radius: 50%; }
  .brand__name { font-family: "Cinzel", serif; font-weight: 400; white-space: nowrap; }
  .brand__cn-row { display: flex; align-items: center; gap: 8px; }
  .brand__rule { flex: 1; height: 1px; }
  .brand__cn { font-family: "Noto Serif TC", serif; font-weight: 600; line-height: 1; }

  /* front */
  .card--front .brand { left: 31px; top: 178px; width: 298px; }
  .card--front .brand__mark { width: 110px; height: 110px; background: var(--mark-grey); }
  .card--front .brand__name { margin-top: 24px; font-size: 20px; letter-spacing: 0.47em; color: var(--ink); padding-left: 0.47em; }
  .card--front .brand__cn-row { margin-top: 0; }
  .card--front .brand__rule { background: var(--rule-front); }
  .card--front .brand__cn { font-size: 22px; color: var(--ink); }

  .contact { position: absolute; left: 402px; top: 75px; font-family: "Nunito Sans", sans-serif; }
  .contact__name, .contact__role { font-size: 14px; letter-spacing: 0.06em; color: var(--ink); font-weight: 400; line-height: 16px; }
  .contact__cn { font-family: "Noto Serif TC", serif; font-weight: 600; font-size: 13px; color: var(--ink); line-height: 15px; }
  .contact__role { margin-top: 15px; }
  .contact__lines { list-style: none; margin-top: 20px; }
  .contact__lines li { font-size: 11px; letter-spacing: 0.1em; color: var(--label); height: 32px; }
  .contact__address { margin-top: 11px; font-size: 15px; font-weight: 300; color: var(--address); line-height: 19px; font-style: normal; letter-spacing: 0.02em; }

  /* back */
  .card--back .glow { position: absolute; left: 185px; top: 20px; width: 310px; height: 290px;
    background: radial-gradient(circle at 50% 50%, var(--glow) 0%, rgba(22,100,170,0.35) 40%, rgba(21,33,68,0) 70%); }
  .card--back .brand { left: 140px; top: 80px; width: 404px; }
  .card--back .brand__mark { width: 150px; height: 150px; background: var(--mark-grey); }
  .card--back .brand__name { margin-top: 20px; font-size: 26px; letter-spacing: 0.54em; color: var(--brand-back); padding-left: 0.54em; }
  .card--back .brand__cn-row { margin-top: 0; }
  .card--back .brand__rule { background: var(--brand-back); }
  .card--back .brand__cn { font-size: 30px; color: var(--brand-back); }
  .tagline { position: absolute; left: 0; right: 0; top: 327px; text-align: center; font-family: "Nunito Sans", sans-serif;
    font-size: 16px; letter-spacing: 0.37em; color: var(--tagline); padding-left: 0.37em; }
</style>
</head>
<body>
<main class="canvas">
  <section class="card card--front" aria-label="Card front">
    <div class="brand">
      <span class="brand__mark" aria-hidden="true"></span>
      <div class="brand__name">LARCH VANTAGE</div>
      <div class="brand__cn-row">
        <span class="brand__rule"></span>
        <span class="brand__cn">嘉信融</span>
        <span class="brand__rule"></span>
      </div>
    </div>
    <div class="contact">
      <div class="contact__name">MORRIS PELHAM</div>
      <div class="contact__cn">彭莫理</div>
      <div class="contact__role">DIRECTOR</div>
      <div class="contact__cn">董事</div>
      <ul class="contact__lines">
        <li>MOBILE:</li>
        <li>EMAIL:</li>
        <li>WEBSITE:</li>
      </ul>
      <address class="contact__address">
        Larch Vantage Pty. Ltd.<br>
        Morris Pelham Director<br>
        Suite 27, 3-9 Quenby St.<br>
        Wendale NSW 2188
      </address>
    </div>
  </section>

  <section class="card card--back" aria-label="Card back">
    <div class="glow" aria-hidden="true"></div>
    <div class="brand">
      <span class="brand__mark" aria-hidden="true"></span>
      <div class="brand__name">LARCH VANTAGE</div>
      <div class="brand__cn-row">
        <span class="brand__rule"></span>
        <span class="brand__cn">嘉信融</span>
        <span class="brand__rule"></span>
      </div>
    </div>
    <p class="tagline">“NAME YOUR OWN TERMS”</p>
  </section>
</main>
</body>
</html>
```